Information poster for parquet showroom

We are a parquet shop from germany and need some information poster for our showroom, to show our costumers some important information about parqut directly. The three posters are about reasons for parquet, and there are two types of paper on the subject. We would like to place the posters in a wooden frame. The design should be modern but simple. Enclosed I send you some of my ideas but it does not have to be like this. Can be completely different. I also send you some pictures of our showroom. 1st poster: Why parquet (dimension: 90x130 cm) Why parquet? - brings nature into your home - ecologically sustainable raw material - pleasantly warm - timeless% 26amp; high quality optics - durable% 26amp; reparable flooring - improved indoor climate - unique ride 2. Advantages oiled - tangible wood structure - natural appearance - scratches less present - partial repair possible advantage varnished - very easy-care - classic% 26amp; elegant appearance - protection against dirt and moisture - variable gloss level 3. Poster: overview of the hardness of different kinds of wood (dimension: 67x130 cm) wood hardness according to Brinell in N / mm² maple europ. 28 maple canadian. 35 birch 27 beech 33 oak 34 alder 17 ash 37 doussie 42 spruce 12 kambala 30 chestnut 18 pine 20 cherry european. 31 Larch 19 Merbau 44 Robinia 48 Sucupira 57 Elm 30 Wenge 45

```html
<!DOCTYPE html>
<html lang="de">
<head>
<meta charset="utf-8">
<title>Parkett Showroom – Infoposter</title>
<link rel="stylesheet" href="https://fonts.googleapis.com/css2?family=Oswald:wght@500;600&family=Roboto+Condensed:wght@400;700&display=swap">
<style>
  :root{
    --orange:#f7931e;
    --ink:#151515;
    --ink-soft:#222;
    --bar-grey:#8c8c8c;
    --white:#fff;
    --paper:#fff;
    --label:#1a1a1a;
  }
  *{box-sizing:border-box;margin:0;padding:0}
  html,body{width:1200px;height:507px;overflow:hidden;background:var(--paper)}
  body{position:relative;font-family:"Oswald",sans-serif}
  .sheet-label{position:absolute;top:37px;font-family:"Roboto Condensed",sans-serif;font-size:18px;color:var(--label);letter-spacing:-.2px}
  .poster{position:absolute;top:65px;height:403px;overflow:hidden;
    background:radial-gradient(ellipse at 50% 45%,#272727 0%,#161616 60%,#0e0e0e 100%)}
  .frame{position:absolute;border:1px solid var(--orange);border-radius:7px}
  .tab{position:absolute;top:0}
  .tab svg{position:absolute;inset:0}
  .tab-title{position:absolute;left:0;right:0;text-align:center;color:var(--white);font-weight:600;text-transform:uppercase;line-height:1}
  .item{position:absolute;color:var(--white);font-weight:500;text-transform:uppercase;line-height:1.06}
  .item .hl{color:var(--orange)}
  .tick{position:absolute}
  /* Poster 1 */
  .why{left:43px;width:279px}
  .why .frame{left:15px;top:24px;width:248px;height:365px}
  .why .tab{left:42px;width:195px;height:38px}
  .why .tab-title{top:9px;font-size:23px;letter-spacing:-.2px}
  .why .item{left:51px;font-size:17.5px;transform:translateY(-9px)}
  .why .tick{left:28px;width:14px;height:14px;transform:translateY(-7px)}
  .showroom-photo{position:absolute;left:16px;top:296px;width:246px;height:92px;border-radius:0 0 7px 7px;
    background:linear-gradient(180deg,#8a9a86 0%,#b9b1a2 35%,#a77f58 70%,#6e5137 100%)}
  /* Poster 2 */
  .oiled{left:346px;width:582px}
  .oiled .frame{left:19px;top:24px;width:541px;height:358px}
  .oiled .tab{height:56px}
  .oiled .tab-title{top:12px;font-size:33px;letter-spacing:-.3px}
  .oiled .divider{position:absolute;left:290px;top:83px;width:1px;height:260px;background:var(--orange)}
  .oiled .item{font-size:25px;line-height:1.02;transform:translateY(-13px)}
  .oiled .tick{width:19px;height:19px;transform:translateY(-9px)}
  /* Poster 3 */
  .hardness{left:958px;width:208px}
  .hardness .room-photo{position:absolute;left:0;right:0;top:200px;bottom:0;
    background:linear-gradient(180deg,rgba(40,40,40,0) 0%,rgba(70,60,50,.35) 60%,rgba(40,34,28,.5) 100%)}
  .hardness .frame{left:9px;top:16px;width:190px;height:375px}
  .hardness .tab{left:42px;width:127px;height:37px}
  .hardness .tab-title{top:6px;font-size:18px}
  .hardness .tab-sub{position:absolute;left:0;right:0;top:24px;text-align:center;font-family:"Roboto Condensed",sans-serif;font-size:7.5px;color:var(--ink)}
  .chart{position:absolute;left:0;top:0}
  .chart text{font-family:"Oswald",sans-serif;font-weight:500;font-size:9.5px;fill:var(--white)}
  .bar-grey{fill:var(--bar-grey)}
  .bar-orange{fill:var(--orange)}
</style>
</head>
<body>
<svg width="0" height="0" style="position:absolute">
  <symbol id="tick" viewBox="0 0 20 20">
    <circle cx="10" cy="10" r="8.6" fill="none" stroke="#f7931e" stroke-width="1.7"/>
    <path d="M6 10.3l2.7 2.7 5.4-5.6" fill="none" stroke="#f7931e" stroke-width="1.8" stroke-linecap="round" stroke-linejoin="round"/>
  </symbol>
</svg>

<div class="sheet-label" style="left:43px">Poster 1</div>
<div class="sheet-label" style="left:346px">Poster 2</div>
<div class="sheet-label" style="left:957px">Poster 3</div>

<!-- Poster 1 -->
<section class="poster why">
  <div class="frame"></div>
  <div class="tab">
    <svg viewBox="0 0 195 38" preserveAspectRatio="none"><path d="M0 0H195L189 30Q187 38 179 38H16Q8 38 6 30Z" fill="var(--orange)"/></svg>
    <div class="tab-title">Warum Parkett ?</div>
  </div>
  <svg class="tick" style="top:63px"><use href="#tick"/></svg>
  <div class="item" style="top:63px">Holt die <span class="hl">Natur</span> in Ihr<br>Zuhause</div>
  <svg class="tick" style="top:109px"><use href="#tick"/></svg>
  <div class="item" style="top:109px"><span class="hl">Ökologisch</span> nachhaltiger<br>Rohstoff</div>
  <svg class="tick" style="top:155px"><use href="#tick"/></svg>
  <div class="item" style="top:155px">Angenehm <span class="hl">fußwarm</span></div>
  <svg class="tick" style="top:182px"><use href="#tick"/></svg>
  <div class="item" style="top:182px"><span class="hl">Zeitlose</span> &amp; hochwertige<br>Optik</div>
  <svg class="tick" style="top:228px"><use href="#tick"/></svg>
  <div class="item" style="top:228px">Langlebiger &amp; <span class="hl">reparabler</span><br>Bodenbelag</div>
  <svg class="tick" style="top:274px"><use href="#tick"/></svg>
  <div class="item" style="top:274px">Einzigartiges <span class="hl">Laufgefühl</span></div>
  <div class="showroom-photo" role="img" aria-label="Foto des Showrooms mit Parkettboden, grünen Sesseln und Zimmerpflanze"></div>
</section>

<!-- Poster 2 -->
<section class="poster oiled">
  <div class="frame"></div>
  <div class="tab" style="left:27px;width:255px">
    <svg viewBox="0 0 255 56" preserveAspectRatio="none"><path d="M0 0H255L247 47Q245 56 236 56H19Q10 56 8 47Z" fill="var(--orange)"/></svg>
    <div class="tab-title">Vorteil geölt</div>
  </div>
  <div class="tab" style="left:306px;width:254px">
    <svg viewBox="0 0 254 56" preserveAspectRatio="none"><path d="M0 0H254L246 47Q244 56 235 56H19Q10 56 8 47Z" fill="var(--orange)"/></svg>
    <div class="tab-title">Vorteil geölt</div>
  </div>
  <div class="divider"></div>

  <svg class="tick" style="left:45px;top:90px"><use href="#tick"/></svg>
  <div class="item" style="left:80px;top:90px">Fühlbare<br>Holzstruktur</div>
  <svg class="tick" style="left:45px;top:157px"><use href="#tick"/></svg>
  <div class="item" style="left:80px;top:157px">Natürliches<br>Aussehen</div>
  <svg class="tick" style="left:45px;top:224px"><use href="#tick"/></svg>
  <div class="item" style="left:80px;top:224px">Kratzer weniger<br>präsent</div>
  <svg class="tick" style="left:45px;top:292px"><use href="#tick"/></svg>
  <div class="item" style="left:80px;top:292px">Partielle<br>Ausbesserung<br>möglich</div>

  <svg class="tick" style="left:323px;top:90px"><use href="#tick"/></svg>
  <div class="item" style="left:359px;top:90px">Sehr<br>pflegeleicht</div>
  <svg class="tick" style="left:323px;top:157px"><use href="#tick"/></svg>
  <div class="item" style="left:359px;top:157px">Klassische &amp;<br>elegante Optik</div>
  <svg class="tick" style="left:323px;top:224px"><use href="#tick"/></svg>
  <div class="item" style="left:359px;top:224px">Schutz<br>gegen Schmutz &amp;<br>Feuchtigkeit</div>
  <svg class="tick" style="left:323px;top:317px"><use href="#tick"/></svg>
  <div class="item" style="left:359px;top:317px">Variierbarer<br>&nbsp;Glanzgrad</div>
</section>

<!-- Poster 3 -->
<section class="poster hardness">
  <div class="room-photo" role="img" aria-label="Dezentes Hintergrundfoto eines Wohnraums mit Parkett"></div>
  <div class="frame"></div>
  <div class="tab">
    <svg viewBox="0 0 127 37" preserveAspectRatio="none"><path d="M0 0H127L121 30Q119 37 112 37H15Q8 37 6 30Z" fill="var(--orange)"/></svg>
    <div class="tab-title">Holzhärte</div>
    <div class="tab-sub">nach Brinell in N/mm²</div>
  </div>
  <svg class="chart" width="208" height="403" viewBox="0 0 208 403">
    <line x1="60" y1="48" x2="60" y2="383" stroke="#fff" stroke-width=".8"/>
    <line x1="60" y1="383" x2="177" y2="383" stroke="#fff" stroke-width=".8"/>
    <g text-anchor="end">
      <text x="53" y="63.5">EICHE</text><text x="53" y="81">BUCHE</text><text x="53" y="98.4">AHORN</text>
      <text x="53" y="115.8">AKAZIE</text><text x="53" y="133.2">ERLE</text><text x="53" y="150.6">LÄRCHE</text>
      <text x="53" y="168">KIEFER</text><text x="53" y="185.4">KIRSCHE</text><text x="53" y="202.8">PAPPEL</text>
      <text x="53" y="220.2">TANNE</text><text x="53" y="237.6">BUCHE</text><text x="53" y="255">AHORN</text>
      <text x="53" y="272.4">AKAZIE</text><text x="53" y="289.8">ERLE</text><text x="53" y="307.2">LÄRCHE</text>
      <text x="53" y="324.6">KIEFER</text><text x="53" y="342">KIRSCHE</text><text x="53" y="359.4">PAPPEL</text>
      <text x="53" y="376.8">TANNE</text>
    </g>
    <g>
      <rect class="bar-grey" x="61" y="55.8" width="108.7" height="8.5"/>
      <rect class="bar-orange" x="61" y="73.2" width="106" height="8.5"/>
      <rect class="bar-grey" x="61" y="90.6" width="100.7" height="8.5"/>
      <rect class="bar-orange" x="61" y="108" width="95.3" height="8.5"/>
      <rect class="bar-grey" x="61" y="125.4" width="90" height="8.5"/>
      <rect class="bar-orange" x="61" y="142.8" width="87.3" height="8.5"/>
      <rect class="bar-grey" x="61" y="160.2" width="81.9" height="8.5"/>
      <rect class="bar-orange" x="61" y="177.6" width="81.9" height="8.5"/>
      <rect class="bar-grey" x="61" y="195" width="81.9" height="8.5"/>
      <rect class="bar-orange" x="61" y="212.4" width="81.9" height="8.5"/>
      <rect class="bar-grey" x="61" y="229.8" width="76.6" height="8.5"/>
      <rect class="bar-orange" x="61" y="247.2" width="71.3" height="8.5"/>
      <rect class="bar-grey" x="61" y="264.6" width="71.3" height="8.5"/>
      <rect class="bar-orange" x="61" y="282" width="68.6" height="8.5"/>
      <rect class="bar-grey" x="61" y="299.4" width="63.3" height="8.5"/>
      <rect class="bar-orange" x="61" y="316.8" width="57.9" height="8.5"/>
      <rect class="bar-grey" x="61" y="334.2" width="57.9" height="8.5"/>
      <rect class="bar-orange" x="61" y="351.6" width="55.3" height="8.5"/>
      <rect class="bar-grey" x="61" y="369" width="55.3" height="8.5"/>
    </g>
    <g>
      <text x="174" y="63.5">45</text><text x="171" y="81">44</text><text x="166" y="98.4">42</text>
      <text x="161" y="115.8">40</text><text x="155" y="133.2">38</text><text x="153" y="150.6">37</text>
      <text x="147" y="168">35</text><text x="147" y="185.4">35</text><text x="147" y="202.8">35</text>
      <text x="147" y="220.2">35</text><text x="142" y="237.6">33</text><text x="137" y="255">31</text>
      <text x="137" y="272.4">31</text><text x="134" y="289.8">30</text><text x="129" y="307.2">28</text>
      <text x="123" y="324.6">26</text><text x="123" y="342">26</text><text x="121" y="359.4">26</text>
      <text x="121" y="376.8">25</text>
    </g>
  </svg>
</section>
</body>
</html>
```